Cobalt Field Services website design

We want to create a Sports turf website for our business Cobalt Field Services - we do sports turf management on sports fields around the Mackay region soccer rugby league softball fields etc from full turf management plans and maintenance to just supply and apply of turf management products and just supply of products with program we also do grounds facility maintenance at council facility's and grounds that require a higher level of care - we will up load our logos and fonts etc to assist with the colour pallet for the website - we will have to have a landing page a shop page with tabs a gallery tab along with a grants initiative and our northreach finest green tab also - our font for the txt is called ethnocentric
Updates

how do we open time for people to submit we have no one submitted

Industry/Entity Type

Turf

Coding

Coded - Design and coding required

Number of Pages Required

5+ page

Font styles to use
Other font styles liked:
• ethnocentric

Requirements
Must have
• I have mentioned some waffle in the description that should assist
Should not have
• anything not related

```html
<!DOCTYPE html>
<html lang="en">
<head>
<meta charset="utf-8">
<title>Cobalt Field Services</title>
<link href="https://fonts.googleapis.com/css2?family=Archivo+Black&family=Domine:wght@400;600&family=Montserrat:wght@400;500;700&family=Open+Sans:wght@400;600&display=swap" rel="stylesheet">
<style>
:root{
  --lime:#9cff00;
  --black:#000;
  --ink:#0b0b0b;
  --white:#fff;
  --muted:#cfcfcf;
  --grass-top:#1d3a12;
  --grass-mid:#2f6b1c;
  --head:"Archivo Black",sans-serif;
  --nav:"Domine",serif;
  --body:"Montserrat",sans-serif;
  --quote:"Open Sans",sans-serif;
}
*{margin:0;padding:0;box-sizing:border-box}
html,body{width:1200px;height:4199px;overflow:hidden;background:var(--black)}
body{position:relative;color:var(--white);font-family:var(--body)}
.abs{position:absolute}
.hl{color:var(--lime)}
.btn{position:absolute;background:var(--lime);color:#000;font-family:var(--head);font-size:12px;border-radius:4px;display:flex;align-items:center;justify-content:center;box-shadow:0 6px 18px rgba(156,255,0,.25)}
.ph{position:absolute}

.logo{font-family:var(--head);font-size:30px;color:var(--white);letter-spacing:1px;display:flex;align-items:center;gap:8px}
.logo i{display:block;width:14px;height:14px;background:var(--lime)}
.nav{position:absolute;left:440px;top:46px;display:flex;gap:6px;font-family:var(--nav);font-size:13px;align-items:center}
.nav a{color:var(--white);text-decoration:none;padding:4px 10px;border-radius:4px}
.nav a.active{background:#2a2a2a}

.hero-word{font-family:var(--head);line-height:1;position:absolute}
.section-title{font-family:var(--head);font-size:40px;line-height:1.08;text-transform:uppercase}
.copy{font-size:11.5px;line-height:1.45;color:var(--muted)}

.bcard{position:absolute;width:236px;height:236px;border:2px solid #ddd;border-radius:18px;background:var(--ink)}
.bcard .icon{position:absolute;left:38px;top:30px;width:160px;height:140px;border-radius:16px;background:#3f6f10}
.bcard span{position:absolute;left:0;right:0;bottom:20px;text-align:center;font-family:var(--head);font-size:15px}

.mlabel{position:absolute;font-family:var(--head);font-size:14px;color:#000}
.mline{position:absolute;height:2px;background:#000}
.mdot{position:absolute;width:11px;height:11px;border-radius:50%;background:#000}

.scard{position:absolute;top:2145px;width:216px;height:292px;border:1px solid #3c6d14;border-radius:6px;background:#050505;overflow:hidden}
.scard.first{border-color:var(--lime)}
.scard .pic{height:145px}
.scard h3{font-family:var(--head);font-size:16px;line-height:1.05;margin:14px 12px 8px;text-transform:uppercase}
.scard p{font-size:12px;line-height:1.45;color:var(--muted);margin:0 12px}
.scard p b{color:var(--lime);font-weight:700}

.review{position:absolute;top:2681px;width:273px;height:204px;background:var(--white);color:#111;border-radius:4px;padding:12px 9px}
.review.dark{background:#000;color:var(--white);border:1px solid var(--lime)}
.stars{color:#ffb800;font-size:14px;letter-spacing:1px}
.review p{font-family:var(--quote);font-size:15px;line-height:1.15;margin-top:6px}
.who{display:flex;gap:8px;align-items:center;margin-top:10px;font-family:var(--quote);font-size:14px;line-height:1.1}
.who i{width:38px;height:38px;border-radius:50%;background:#4a4a4a;flex:none}
.avatar{position:absolute;top:2614px;width:40px;height:40px;border-radius:50%;background:#8a8a8a;border:2px solid #fff}

.flinks{position:absolute;left:719px;top:3918px;font-family:var(--nav);font-size:12.5px;line-height:25px}
.contact{position:absolute;left:885px;font-size:13px;line-height:1.3;display:flex;gap:10px}
.contact svg{flex:none}
.social{position:absolute;top:3744px;width:36px;height:36px;border-radius:50%;background:var(--lime)}
</style>
</head>
<body>

<div class="logo abs" style="left:150px;top:40px"><i></i>CFS</div>
<nav class="nav">
  <a class="active">Home</a><a>About Us</a><a>Shop</a><a>Gallery Tab</a><a>Northreach Finest Green</a><a>Grants Initiative</a>
  <svg width="14" height="16" viewBox="0 0 14 16"><circle cx="7" cy="4" r="3.5" fill="#9cff00"/><path d="M0 16c0-5 3-7 7-7s7 2 7 7z" fill="#9cff00"/></svg>
</nav>

<div class="ph" role="img" aria-label="Stadium floodlights, left" style="left:0;top:70px;width:150px;height:130px;background:radial-gradient(ellipse at 40% 40%,rgba(255,255,255,.55),rgba(0,0,0,0) 70%)"></div>
<div class="ph" role="img" aria-label="Stadium floodlights, right" style="left:1030px;top:40px;width:170px;height:180px;background:radial-gradient(ellipse at 60% 40%,rgba(255,255,255,.55),rgba(0,0,0,0) 70%)"></div>
<div class="ph" role="img" aria-label="Floodlit grass pitch" style="left:0;top:440px;width:1200px;height:180px;background:linear-gradient(180deg,#000 0%,var(--grass-top) 30%,var(--grass-mid) 75%,#244f15 100%)"></div>
<div class="hero-word" style="left:320px;top:228px;font-size:106px">READY</div>
<div class="hero-word hl" style="left:738px;top:292px;font-size:28px">TO</div>
<div class="hero-word hl" style="left:583px;top:318px;font-size:108px">PLAY</div>
<div class="ph" role="img" aria-label="Tennis ball" style="left:735px;top:238px;width:32px;height:32px;border-radius:50%;background:var(--lime)"></div>
<div class="ph" role="img" aria-label="Shuttlecock" style="left:272px;top:340px;width:62px;height:60px;background:#2f4a0a"></div>
<div class="ph" role="img" aria-label="Soccer ball" style="left:868px;top:442px;width:58px;height:58px;border-radius:50%;background:#cfcfcf"></div>
<div class="btn" style="left:533px;top:482px;width:135px;height:36px">SHOP NOW</div>

<h2 class="section-title abs" style="left:150px;top:688px">BENEFITS OF<br>CHOOSING<br><span class="hl">US</span></h2>
<p class="copy abs" style="left:150px;top:826px;width:345px">There Are Many Variations Of Passages Of Lorem Available, But The Majority Have Suffered Alteration In Some Form, By Injected Humour, Or Randomised Which Don't Look Even Slightly Believable. If You Are Going To Use A Passage Of Lorem Ipsum, You Need To Be Sure There Isn't Anything.</p>
<div class="btn" style="left:150px;top:950px;width:135px;height:36px">SHOP NOW</div>

<div class="bcard" style="left:542px;top:697px;transform:rotate(9deg)"><div class="icon" role="img" aria-label="Sports equipment icon"></div><span>TURF PRODUCTS</span></div>
<div class="bcard" style="left:795px;top:713px;transform:rotate(-6deg)"><div class="icon" role="img" aria-label="Lawn mower icon"></div><span>LEVEL OF CARE</span></div>
<div class="bcard" style="left:534px;top:958px;transform:rotate(22deg)"><div class="icon" role="img" aria-label="Pitch layout icon"></div><span>TURF MAINTENANCE</span></div>
<div class="bcard" style="left:790px;top:974px;transform:rotate(6deg)"><div class="icon" role="img" aria-label="Idea and gears icon"></div><span>TURF MANAGEMENT</span></div>

<svg class="abs" style="left:0;top:1299px" width="1200" height="546" viewBox="0 0 1200 546">
  <path d="M0 83 H680 C710 83 715 0 760 0 H1200 V546 H0Z" fill="#9cff00"/>
</svg>
<h2 class="section-title abs" style="left:150px;top:1322px;font-size:38px">OUR PRODUCT <span class="hl">MATERIAL</span></h2>
<p class="abs" style="left:773px;top:1307px;width:290px;font-size:11.5px;line-height:1.45;color:#111">There Are Many Variations Of Passages Of Available, But The Majority Have Suffered Some Form, By Injected Humour, Or Ran Words&nbsp; Don't Look Even Slightly Believable.</p>
<div class="ph" role="img" aria-label="Cross-section of turf layers: artificial grass, weed barrier, shock pad and compacted base" style="left:160px;top:1425px;width:520px;height:380px;border-radius:8px;background:linear-gradient(180deg,#4f9a2c,#7fc21a)"></div>
<div class="mline" style="left:700px;top:1505px;width:180px"></div><div class="mdot" style="left:874px;top:1501px"></div><div class="mlabel" style="left:897px;top:1497px">ARTIFICIAL GRASS</div>
<div class="mline" style="left:700px;top:1554px;width:180px"></div><div class="mdot" style="left:874px;top:1550px"></div><div class="mlabel" style="left:897px;top:1546px">WEED BARRIER</div>
<div class="mline" style="left:700px;top:1616px;width:175px"></div><div class="mdot" style="left:869px;top:1612px"></div><div class="mlabel" style="left:892px;top:1608px">SHOCKPAD</div>
<div class="mline" style="left:700px;top:1741px;width:180px"></div><div class="mdot" style="left:874px;top:1737px"></div><div class="mlabel" style="left:897px;top:1733px">COMPACTED BASE</div>

<h2 class="section-title abs" style="left:0;width:1200px;top:1915px;text-align:center;font-size:38px">SHOP OUR TURF<br><span class="hl">MANAGEMENT</span></h2>
<p class="copy abs" style="left:230px;width:740px;top:2010px;text-align:center;font-size:12px">There Are Many Variations Of Passages Of Lorem Ipsum Available, But The Majority Have Suffered Alteration In Some Form, By Injected Hum Our, Or Rando Mised Words Which Don't Look Even Slightly Believable.</p>
<div class="btn" style="left:532px;top:2072px;width:136px;height:35px">SHOP NOW</div>

<div class="scard first" style="left:158px"><div class="pic" role="img" aria-label="Floodlit sports field" style="background:linear-gradient(180deg,#9fc1d8,#4f8a2a)"></div><h3>Turf Management Plans</h3><p>There Are Many Variations Of Passages Of Lorem Ipsum Available, But The Majority Have Suffered <b>Read More .</b></p></div>
<div class="scard" style="left:381px"><div class="pic" role="img" aria-label="Groundskeeper tending grass" style="background:linear-gradient(180deg,#5f7d3a,#3f6e25)"></div><h3>Grounds Maintenance</h3><p>There Are Many Variations Of Passages Of Lorem Ipsum Available, But The Majority Have Suffered <b>Read More .</b></p></div>
<div class="scard" style="left:603px"><div class="pic" role="img" aria-label="Roll of turf on soil" style="background:linear-gradient(180deg,#3b7a24,#5a3a26)"></div><h3>Turf Management Products</h3><p>There Are Many Variations Of Passages Of Lorem Ipsum Available, But The Majority Have Suffered <b>Read More .</b></p></div>
<div class="scard" style="left:825px"><div class="pic" role="img" aria-label="Hands laying turf" style="background:linear-gradient(180deg,#6b5a4a,#3f6e25)"></div><h3>Turf Ground Plans</h3><p>There Are Many Variations Of Passages Of Lorem Ipsum Available, But The Majority Have Suffered <b>Read More .</b></p></div>

<h2 class="section-title abs" style="left:150px;top:2507px;font-size:42px">OUR HAPPY<br><span class="hl">CLIENTS</span></h2>
<div class="avatar" role="img" aria-label="Client portrait" style="left:150px"></div>
<div class="avatar" role="img" aria-label="Client portrait" style="left:186px"></div>
<div class="avatar" role="img" aria-label="Client portrait" style="left:222px"></div>
<div class="avatar" role="img" aria-label="Client portrait" style="left:258px"></div>
<div class="abs" style="left:800px;top:2510px;width:250px;text-align:right;font-family:var(--quote)">
  <div style="font-size:34px;font-weight:600;color:var(--white);line-height:1.1">ReviewHub</div>
  <div style="font-size:18px;margin-top:4px;white-space:nowrap">Customer Review 4.9</div>
</div>

<div class="review" style="left:183px"><div class="stars">★★★★★</div><p>Lorem Ipsum Dolor Sit Amet, Adipiscing Elit,Sed Do Eiusmod Incididunt Ut Labore Et Dolore Aliqua. Ut Enim Ad Minimveniam, Nostrud Exercitation.Ut Enim Veniam, Nostrud Exercitation</p><div class="who"><i role="img" aria-label="Reviewer portrait"></i><div>Mara Ellis<br>Software Development</div></div></div>
<div class="review dark" style="left:463px"><div class="stars">★★★★★</div><p>Lorem Ipsum Dolor Sit Amet, Adipiscing Elit,Sed Do Eiusmod Incididunt Ut Labore Et Dolore Aliqua. Ut Enim Ad Minimveniam, Nostrud Exercitation.Ut Enim Veniam, Nostrud Exercitation</p><div class="who"><i role="img" aria-label="Reviewer portrait"></i><div>Mara Ellis<br>Software Development</div></div></div>
<div class="review" style="left:742px"><div class="stars">★★★★★</div><p>Lorem Ipsum Dolor Sit Amet, Adipiscing Elit,Sed Do Eiusmod Incididunt Ut Labore Et Dolore Aliqua. Ut Enim Ad Minimveniam, Nostrud Exercitation.Ut Enim Veniam, Nostrud Exercitation</p><div class="who"><i role="img" aria-label="Reviewer portrait"></i><div>Mara Ellis<br>Software Development</div></div></div>
<svg class="abs" style="left:570px;top:2898px" width="60" height="8"><circle cx="4" cy="4" r="2.5" fill="#fff"/><rect x="14" y="3" width="14" height="2.5" rx="1.2" fill="#9cff00"/><circle cx="40" cy="4" r="2.5" fill="#fff"/><circle cx="52" cy="4" r="2.5" fill="#fff"/></svg>

<div class="ph" role="img" aria-label="Faint diagonal stripes" style="left:0;top:2960px;width:1200px;height:560px;background:linear-gradient(135deg,#050505,#111)"></div>
<h2 class="section-title abs" style="left:0;width:1200px;top:2994px;text-align:center;font-size:40px">OUR GALLERY <span class="hl">SHORTS</span></h2>
<div class="ph" role="img" aria-label="Gallery strip of stadium, running track and grass photos" style="left:272px;top:3088px;width:200px;height:330px;border-radius:8px;background:linear-gradient(90deg,#5a4a40,#3c8a22)"></div>
<div class="ph" role="img" aria-label="Hands trimming a green hedge with secateurs" style="left:432px;top:3088px;width:498px;height:350px;border-radius:10px;background:linear-gradient(180deg,#5f8f3a,#24521a)"></div>
<div class="abs" style="left:519px;top:3458px;width:30px;height:30px;border-radius:50%;background:var(--lime)"><svg width="30" height="30"><path d="M17 9l-6 6 6 6" stroke="#000" stroke-width="2.5" fill="none"/></svg></div>
<div class="abs" style="left:569px;top:3458px;width:30px;height:30px;border-radius:50%;background:var(--lime)"><svg width="30" height="30"><path d="M13 9l6 6-6 6" stroke="#000" stroke-width="2.5" fill="none"/></svg></div>

<h2 class="section-title abs" style="left:0;width:1200px;top:3580px;text-align:center;font-size:40px">SIGN UP FOR OUR NEWSLATTER</h2>
<p class="copy abs" style="left:0;width:1200px;top:3632px;text-align:center;font-size:12px">There Are Many Variations Of Passages Of Lorem Ipsum Available, But The Majority Have Believable.</p>
<div class="abs" style="left:358px;top:3680px;width:484px;height:46px;border:1.5px solid #bbb;border-radius:6px"></div>
<div class="btn" style="left:691px;top:3683px;width:148px;height:40px">SUBSCRIBE NOW</div>
<div class="social" role="img" aria-label="Social link" style="left:509px"></div>
<div class="social" role="img" aria-label="Social link" style="left:557px"></div>
<div class="social" role="img" aria-label="Social link" style="left:606px"></div>
<div class="social" role="img" aria-label="Social link" style="left:654px"></div>

<div class="logo abs" style="left:150px;top:3848px"><i></i>CFS</div>
<p class="abs" style="left:150px;top:3925px;width:230px;font-family:var(--nav);font-size:11.5px;line-height:1.45;color:var(--muted)">It Is A Long Established Fact That A Reader Will Be Distracted By The Readable Content Of A Page When Looking At Its Layout.</p>
<div class="flinks">About Us<br>Shop<br>Gallery Tab<br>Northreach Finest Green<br>Grants Initiative</div>
<div class="contact" style="top:3962px"><svg width="14" height="16" viewBox="0 0 14 16"><path d="M7 0a6 6 0 00-6 6c0 4.5 6 10 6 10s6-5.5 6-10a6 6 0 00-6-6z" fill="#9cff00"/><circle cx="7" cy="6" r="2.2" fill="#000"/></svg><span style="font-family:var(--nav)">48 Harbour Row,<br>Eastvale</span></div>
<div class="contact" style="top:4000px"><svg width="16" height="12" viewBox="0 0 16 12"><rect width="16" height="12" rx="1.5" fill="#9cff00"/><path d="M1 1l7 6 7-6" stroke="#000" stroke-width="1.4" fill="none"/></svg><span>info@cobaltfield.com</span></div>
<div class="contact" style="top:4028px"><svg width="15" height="15" viewBox="0 0 24 24"><path d="M6.6 10.8a15 15 0 006.6 6.6l2.2-2.2a1 1 0 011-.25 11.4 11.4 0 003.6.57 1 1 0 011 1V20a1 1 0 01-1 1A17 17 0 013 4a1 1 0 011-1h3.5a1 1 0 011 1 11.4 11.4 0 00.57 3.6 1 1 0 01-.25 1z" fill="#9cff00"/></svg><span>(+11) 555 210 387</span></div>
<div class="abs" style="left:0;width:1200px;top:4062px;text-align:center;font-family:var(--head);font-size:50px;letter-spacing:1px;color:#3a3a3a">COBALT FIELD SERVICES</div>
<div class="abs" style="left:0;top:4140px;width:1200px;height:1px;background:#555"></div>
<p class="abs" style="left:0;width:1200px;top:4165px;text-align:center;font-size:11.5px;color:var(--muted)">Copyright 2025 CFS All Rights Reserved</p>

</body>
</html>
```